Bellcove Realty Business Cards
Business Cards design
Professional
Marnie Toskovic
Licensed Broker
482 Linwell Ave
San Francisco, CA 94387
marnie@bellcoverealty.com
www.bellcoverealty.com
DRE#07391826
Include photo on front of card
- Experienced Mortgage Consultant
- Residential Listings
- Short Sale Expertise
- Property Management
Logo
Headshot

```html
<!DOCTYPE html>
<html lang="en">
<head>
<meta charset="utf-8">
<title>Bellcove Realty – Business Card</title>
<link rel="stylesheet" href="https://fonts.googleapis.com/css2?family=Arimo:wght@400;700&display=swap">
<style>
  :root {
    --paper: #ffffff;
    --brand-red: #f11a12;
    --brand-navy: #1f1f7a;
    --ink: #111111;
    --muted: #7a7a7a;
    --rule: #b5b5b5;
    --crop: #9a9a9a;
    --photo-top: #d9dbe4;
    --photo-bottom: #a9adbf;
  }
  * { margin: 0; padding: 0; box-sizing: border-box; }
  html, body {
    width: 1200px; height: 766px; overflow: hidden;
    background: var(--paper);
    font-family: "Arimo", Arial, sans-serif;
  }
  .sheet { position: relative; width: 1200px; height: 766px; }
  .crop-marks { position: absolute; inset: 0; }
  .card {
    position: absolute; left: 96px; top: 91px;
    width: 1008px; height: 576px;
    overflow: hidden;
    background: var(--brand-red);
  }
  .card-backdrop { position: absolute; inset: 0; }
  .brand-name {
    position: absolute; left: 0; right: 0; top: 150px;
    text-align: center;
    font-weight: 700; font-size: 82px; letter-spacing: 1px;
    color: var(--brand-navy);
  }
  .divider {
    position: absolute; left: 499px; top: 305px;
    width: 2px; height: 240px;
    background: linear-gradient(var(--rule), rgba(181,181,181,0));
  }
  .contact {
    position: absolute; right: 530px; top: 300px;
    text-align: right; list-style: none;
    font-size: 21px; line-height: 27px;
    color: var(--muted);
    white-space: nowrap;
  }
  .headshot {
    position: absolute; left: 532px; top: 318px;
    width: 118px; height: 118px; border-radius: 50%;
    background: linear-gradient(var(--photo-top), var(--photo-bottom));
    border: 3px solid var(--brand-navy);
  }
  .person { position: absolute; left: 672px; top: 318px; white-space: nowrap; }
  .person-name { font-size: 34px; color: var(--ink); font-weight: 400; }
  .person-title { font-size: 22px; color: var(--muted); margin-top: 4px; }
  .services {
    list-style: none; margin-top: 10px;
    font-size: 15px; line-height: 19px; color: var(--muted);
  }
  .services li::before { content: "• "; color: var(--brand-red); }
</style>
</head>
<body>
<div class="sheet">
  <svg class="crop-marks" width="1200" height="766" viewBox="0 0 1200 766" aria-hidden="true">
    <g stroke="var(--crop)" stroke-width="1.5">
      <line x1="96" y1="0" x2="96" y2="60"/>
      <line x1="1104" y1="0" x2="1104" y2="60"/>
      <line x1="96" y1="703" x2="96" y2="766"/>
      <line x1="1104" y1="703" x2="1104" y2="766"/>
      <line x1="0" y1="91" x2="60" y2="91"/>
      <line x1="1140" y1="91" x2="1200" y2="91"/>
      <line x1="0" y1="667" x2="60" y2="667"/>
      <line x1="1140" y1="667" x2="1200" y2="667"/>
    </g>
  </svg>

  <section class="card">
    <svg class="card-backdrop" width="1008" height="576" viewBox="0 0 1008 576" aria-hidden="true">
      <ellipse cx="504" cy="290" rx="640" ry="266" fill="var(--paper)" stroke="var(--brand-navy)" stroke-width="7"/>
    </svg>

    <h1 class="brand-name">Bellcove Realty</h1>

    <div class="divider"></div>

    <ul class="contact">
      <li>482 Linwell Ave</li>
      <li>San Francisco, CA 94387</li>
      <li>Phone: XXX-XXX-XXX</li>
      <li>Fax: XXX-XXX-XXX</li>
      <li>E-mail: marnie@bellcoverealty.com</li>
      <li>www.bellcoverealty.com</li>
      <li>DRE#07391826</li>
    </ul>

    <div class="headshot" role="img" aria-label="Headshot photo of Marnie Toskovic"></div>

    <div class="person">
      <p class="person-name">Marnie Toskovic</p>
      <p class="person-title">Licensed Broker</p>
      <ul class="services">
        <li>Experienced Mortgage Consultant</li>
        <li>Residential Listings</li>
        <li>Short Sale Expertise</li>
        <li>Property Management</li>
      </ul>
    </div>
  </section>
</div>
</body>
</html>
```